Commercial Real Estate Executive Recruiting Firm Needs Business Card Design

We need a business card design for BRAMLEY | Executive Recruiting - an executive recruiting firm focused exclusively on the commercial real estate industry. We place professionals ranging from Analyst to the Executive Office covering all investment/finance disciplines (acquisitions, asset management, capital markets, etc.) in all product types (office, retail, multifamily, industrial, land, etc.). We have a passion for helping people (clients and candidates) and have a reputation for being open and honest in our recruiting - and yes, very successful. We have recently developed a new logo and would like to update our business cards as well. I've uploaded some information about our company that contains the new logo.

Target Market(s)

Commercial Real Estate professionals. Primarily in the US. These are typically, smart, driven professionals with finance degrees and MBAs. Primarily men between the ages of 25 and 55.

Industry/Entity Type

Real Estate

Font styles to use
Other font styles liked:
• The font for "BRAMLEY" is Blair ITC (Medium), and "executive recruiting" is Gotham (Book).

Requirements
Must have
• I like the idea of white background on one side and solid color (blue, black, etc.) on back of card.

Would like to utilize the fonts in the logo (to the extent possible) so as to not have too many fonts on card.
Nice to have
• I think the roles (i.e., Acquisitions, Asset Management, etc.,...) is probably likely best placed on the back side of the card with the logo maybe. See attached current business card for content.

```html
<!DOCTYPE html>
<html lang="en">
<head>
<meta charset="utf-8">
<title>BRAMLEY | Executive Recruiting — Business Card</title>
<link href="https://fonts.googleapis.com/css2?family=Montserrat:ital,wght@0,400;0,500;1,400&display=swap" rel="stylesheet">
<style>
  :root {
    --backdrop: #a4a4a4;
    --card-light: #fbfbf2;
    --card-dark: #3b3b3d;
    --ink-dark: #4a4a4c;
    --ink-light: #f4f4f4;
    --ink-muted: #d2d2d2;
  }
  * { margin: 0; padding: 0; box-sizing: border-box; }
  html, body {
    width: 1200px; height: 960px; overflow: hidden;
    background: var(--backdrop);
    font-family: "Montserrat", Arial, sans-serif;
  }
  .stage {
    width: 1200px; height: 960px;
    display: flex; align-items: center; justify-content: center; gap: 40px;
  }
  .card {
    width: 540px; height: 309px; position: relative; overflow: hidden; flex: none;
    box-shadow: 0 10px 28px rgba(0,0,0,.25);
    white-space: nowrap;
  }
  /* Front */
  .card-front { background: var(--card-light); display: flex; flex-direction: column; }
  .front-top { flex: 0 0 180px; display: flex; flex-direction: column; align-items: center; padding-top: 36px; }
  .wordmark {
    display: flex; align-items: center; gap: 12px;
    font-weight: 500; letter-spacing: 3px; font-size: 18px;
  }
  .wordmark-square { width: 28px; height: 28px; background: currentColor; flex: none; }
  .card-front .wordmark { color: var(--ink-dark); }
  .specialty {
    margin-top: 34px; font-size: 13.5px; font-weight: 500; color: #2e2e30; letter-spacing: .4px;
  }
  .specialty-note { margin-top: 4px; font-size: 11.5px; font-style: italic; color: #3a3a3c; }
  .front-band {
    flex: 1; background: var(--card-dark); color: var(--ink-light);
    display: flex; align-items: center; padding: 0 18px 0 22px; gap: 16px;
  }
  .person { display: flex; flex-direction: column; align-items: flex-end; flex: none; }
  .person-name { font-size: 21px; font-weight: 500; }
  .person-title { font-size: 13px; margin-top: 2px; }
  .contact-phone, .contact-item { display: flex; align-items: center; gap: 6px; flex: none; }
  .contact-phone { font-size: 11.5px; }
  .contact-list { display: flex; flex-direction: column; gap: 10px; margin-left: auto; flex: none; }
  .contact-item { font-size: 9px; }
  .icon { width: 14px; height: 14px; flex: none; }
  /* Back */
  .card-back {
    background: var(--card-dark); color: var(--ink-light);
    display: flex; flex-direction: column; align-items: center; justify-content: center;
  }
  .card-back .wordmark { color: var(--ink-light); }
  .disciplines { margin-top: 14px; font-size: 9px; color: var(--ink-muted); letter-spacing: .4px; }
</style>
</head>
<body>
<main class="stage">
  <section class="card card-front" aria-label="Card front">
    <div class="front-top">
      <div class="wordmark"><span class="wordmark-square"></span>BRAMLEY | Executive Recruiting</div>
      <p class="specialty">COMMERCIAL REAL ESTATE RECRUITING</p>
      <p class="specialty-note">Analyst to Executive Office Placement</p>
    </div>
    <div class="front-band">
      <div class="person">
        <span class="person-name">JORDAN HALE</span>
        <span class="person-title">President</span>
      </div>
      <div class="contact-phone">
        <svg class="icon" viewBox="0 0 14 14"><rect x="1" y="1" width="12" height="12" rx="2" fill="var(--ink-light)"/><path d="M5 3.5c-.8.4-1 1.4-.6 2.6.6 1.8 1.9 3.4 3.4 4.2.9.4 1.7.3 2.1-.3l-1.2-1.4-1 .5C6.9 8.5 6 7.4 5.6 6.4l.9-.7z" fill="var(--card-dark)"/></svg>
        <span>M | 214-555-0148</span>
      </div>
      <div class="contact-list">
        <div class="contact-item">
          <svg class="icon" viewBox="0 0 14 14"><rect x="1" y="3" width="12" height="8" fill="none" stroke="var(--ink-light)" stroke-width="1.2"/><path d="M1 3l6 5 6-5" fill="none" stroke="var(--ink-light)" stroke-width="1.2"/></svg>
          <span>jordan@bramleyrecruiting.com</span>
        </div>
        <div class="contact-item">
          <svg class="icon" viewBox="0 0 14 14"><rect x="0.5" y="0.5" width="13" height="13" rx="2" fill="var(--ink-light)"/><circle cx="7" cy="7" r="4.3" fill="none" stroke="var(--card-dark)"/><ellipse cx="7" cy="7" rx="1.8" ry="4.3" fill="none" stroke="var(--card-dark)"/><path d="M2.7 7h8.6" stroke="var(--card-dark)"/></svg>
          <span>www.bramleyrecruiting.com</span>
        </div>
      </div>
    </div>
  </section>

  <section class="card card-back" aria-label="Card back">
    <div class="wordmark"><span class="wordmark-square"></span>BRAMLEY | Executive Recruiting</div>
    <p class="disciplines">Acquisitions | Asset Management | Banking | Development | Capital Markets | Brokerage</p>
  </section>
</main>
</body>
</html>
```